Sports Therapy and Personal Training

I need a business card design for a new business based in Toronto called "Holbrin Athletics" I am a sports therapist as well as a strength and conditioning coach, therefore I work mainly with high level athletes and physically active people. I am starting my own therapy/training business. The services I will be offering include fitness consultation, personal training, athlete assessments, and rehabilitation therapy. These services will be delivered in peoples homes and/or a facility in which I rent space.

The final design should communicate "high-end" and "quality"

Target Market(s)

athletes and physically active people

Industry/Entity Type

Fitness

Requirements
Must have
• 1. The business logo - files attached

2. my name and credentials

Derek Falloway - CAT(C), CK, CSCS,

Certified Athletic Therapist
Strength and Conditioning Specialist

3. website - www.holbrinathletics.example

4. email address - derek@holbrinathletics.example

5. phone number

```html
<!DOCTYPE html>
<html lang="en">
<head>
<meta charset="utf-8">
<title>Holbrin Athletics – Business Card</title>
<link rel="stylesheet" href="https://fonts.googleapis.com/css2?family=Michroma&family=Russo+One&family=Open+Sans:wght@800&display=swap">
<style>
  :root {
    --card-white: #ffffff;
    --card-grey-light: #ececec;
    --card-grey-mid: #c9c9c9;
    --brand-dark: #2e2e30;
    --brand-red: #e3262a;
    --tagline-grey: #8a8a8c;
    --text-black: #111111;
    --band-dark: #3a3b3e;
    --band-light: #8d8f93;
  }
  * { margin: 0; padding: 0; box-sizing: border-box; }
  html, body {
    width: 1200px; height: 733px; overflow: hidden;
    background: var(--card-white);
  }
  .card {
    position: relative; width: 1200px; height: 733px; overflow: hidden;
    background: linear-gradient(180deg, var(--card-white) 0%, var(--card-white) 36%, #f7f7f7 50%, var(--card-grey-light) 78%, var(--card-grey-mid) 100%);
    font-family: "Open Sans", Verdana, sans-serif;
  }
  .brand {
    position: absolute; left: 40px; top: 40px;
    display: flex; align-items: center; gap: 34px;
  }
  .brand-mark {
    width: 170px; height: 170px; border-radius: 50%;
    background: var(--brand-dark);
  }
  .brand-text { display: flex; flex-direction: column; gap: 18px; }
  .brand-name {
    font-family: "Michroma", sans-serif;
    font-size: 50px; line-height: 1; letter-spacing: 1px;
    text-transform: uppercase; color: var(--brand-dark);
  }
  .brand-tagline {
    font-family: "Michroma", sans-serif;
    font-size: 25px; line-height: 1; letter-spacing: 0.5px;
    text-transform: uppercase; color: var(--tagline-grey);
  }
  .mesh-band {
    position: absolute; left: 0; top: 264px; width: 1200px; height: 70px;
    background: linear-gradient(180deg, var(--band-light) 0%, var(--band-dark) 30%, #55575b 60%, var(--band-dark) 100%);
    box-shadow: 0 4px 10px rgba(0,0,0,0.25);
  }
  .person { position: absolute; left: 31px; top: 368px; }
  .person-name {
    font-family: "Russo One", sans-serif;
    font-size: 46px; line-height: 1; letter-spacing: 3px;
    text-transform: uppercase; color: var(--brand-red);
    text-shadow: 0 0 6px rgba(227,38,42,0.45);
  }
  .credentials {
    margin-top: 40px; list-style: none;
    font-size: 25px; line-height: 37px; color: var(--text-black);
  }
  .contact {
    position: absolute; left: 567px; top: 620px; list-style: none;
    font-size: 25px; line-height: 34px; color: var(--text-black);
    text-shadow: 1px 1px 0 var(--card-white);
  }
</style>
</head>
<body>
  <main class="card">
    <header class="brand">
      <div class="brand-mark" aria-hidden="true"></div>
      <div class="brand-text">
        <div class="brand-name">Holbrin Athletics</div>
        <div class="brand-tagline">Sports Medicine ▪ Strength and Conditioning</div>
      </div>
    </header>

    <div class="mesh-band" role="img" aria-label="Dark metallic mesh band across the card"></div>

    <section class="person">
      <h1 class="person-name">Derek Falloway</h1>
      <ul class="credentials">
        <li>CAT(C), CK, CSCS</li>
        <li>Certified Athletic Therapist</li>
        <li>Strength and Conditioning Specialist</li>
      </ul>
    </section>

    <ul class="contact">
      <li>Visit - www.holbrinathletics.example</li>
      <li>Email - derek@holbrinathletics.example</li>
      <li>Phone - 000 000 000</li>
    </ul>
  </main>
</body>
</html>
```